Comprehensive guide for the front desk medical office staff.

selling a reference guide for the front desk personnel at Urgent Care clinics

Target Market(s)

Urgent Care and physian office manager s

Industry/Entity Type

Medical

```html
<!DOCTYPE html>
<html lang="en">
<head>
<meta charset="utf-8">
<title>Intake Desk Companion Guide – Postcard</title>
<link rel="stylesheet" href="https://fonts.googleapis.com/css2?family=Oswald:wght@500;700&family=Mulish:ital,wght@0,400;0,600;1,400;1,700&display=swap">
<style>
  :root {
    --navy-deep: #0c2a5c;
    --navy: #123a7a;
    --blue: #1560b8;
    --blue-bright: #1f78d1;
    --yellow: #fff23a;
    --white: #ffffff;
    --page: #ffffff;
    --rule: #c9cf5a;
  }
  * { box-sizing: border-box; margin: 0; padding: 0; }
  html, body { width: 912px; height: 1200px; overflow: hidden; background: var(--page); }
  body { position: relative; font-family: "Mulish", Arial, sans-serif; color: var(--white); }

  .card { position: absolute; left: 33px; width: 824px; height: 550px; overflow: hidden; background: var(--white); }
  .card--front { top: 31px; }
  .card--back { top: 597px; }
  .card__shapes { position: absolute; inset: 0; }

  .panel { position: absolute; left: 0; top: 0; text-align: center; }
  .card--front .panel { width: 345px; padding-top: 42px; }
  .card--back .panel { width: 300px; padding-top: 34px; padding-left: 46px; text-align: left; }

  .intro { font-style: italic; font-size: 14px; margin-bottom: 12px; }
  .rule { height: 1px; background: var(--rule); margin: 0 auto; width: 240px; }
  .card--back .rule { margin: 0; width: 256px; }

  .title { font-family: "Oswald", "Arial Narrow", sans-serif; font-weight: 700; color: var(--yellow); line-height: 1.08; }
  .title__main { font-size: 29px; letter-spacing: 0.2px; }
  .title__sub { font-family: "Oswald", "Arial Narrow", sans-serif; font-weight: 500; font-size: 18px; line-height: 1.25; margin-top: 2px; color: var(--yellow); }
  .title-block { padding: 8px 0 6px; }
  .card--back .title-block { text-align: center; width: 256px; }

  .body-copy { font-style: italic; font-size: 15.5px; line-height: 1.3; padding: 10px 46px 0; }

  .order { margin-top: 12px; }
  .order__label { font-style: italic; font-weight: 700; font-size: 15px; }
  .order__phone { font-family: "Oswald", "Arial Narrow", sans-serif; font-weight: 700; font-size: 30px; color: var(--yellow); line-height: 1.15; }
  .order__price { font-size: 20px; line-height: 1.2; }
  .order__price sup { font-size: 11px; }
  .order__shipping { font-style: italic; font-size: 14px; margin-top: 2px; }

  .headline { position: absolute; left: 345px; right: 0; top: 422px; text-align: center; }
  .headline__main { font-family: "Oswald", "Arial Narrow", sans-serif; font-weight: 700; font-size: 29px; line-height: 1.12; color: var(--yellow); }
  .headline__tag { font-style: italic; font-weight: 700; font-size: 19px; color: var(--yellow); margin-top: 8px; }

  .lead { font-style: italic; font-size: 17.5px; line-height: 1.38; margin-top: 12px; width: 265px; }
  .features { list-style: none; margin-top: 16px; font-size: 14px; line-height: 1.55; width: 265px; }
  .features li { position: relative; padding-left: 22px; }
  .features svg { position: absolute; left: 0; top: 4px; }
  .more { font-style: italic; font-weight: 700; font-size: 13.5px; text-align: center; margin-top: 4px; width: 265px; }

  .badge { position: absolute; left: 313px; top: 11px; width: 190px; height: 190px; border-radius: 50%; border: 4px solid var(--yellow);
           background: radial-gradient(circle at 50% 40%, var(--blue-bright), var(--navy) 85%); text-align: center; padding-top: 34px; }
  .badge__label { font-size: 18px; font-style: italic; }
  .badge__phone { font-family: "Oswald", "Arial Narrow", sans-serif; font-weight: 700; font-size: 27px; color: var(--yellow); line-height: 1.15; }
  .badge__price { font-size: 18px; }
  .badge__price sup { font-size: 10px; }
  .badge__shipping { font-size: 14px; line-height: 1.3; }
</style>
</head>
<body>

<section class="card card--front">
  <svg class="card__shapes" width="824" height="550" viewBox="0 0 824 550">
    <defs>
      <linearGradient id="front-panel" x1="0" y1="0" x2="1" y2="1">
        <stop offset="0" stop-color="#0b2657"/><stop offset="0.6" stop-color="#143f85"/><stop offset="1" stop-color="#0c2a5c"/>
      </linearGradient>
      <linearGradient id="front-band" x1="0" y1="0" x2="1" y2="0">
        <stop offset="0" stop-color="#0f4ea3"/><stop offset="0.5" stop-color="#1f78d1"/><stop offset="1" stop-color="#1258b0"/>
      </linearGradient>
      <linearGradient id="front-photo" x1="0" y1="0" x2="1" y2="1">
        <stop offset="0" stop-color="#e9e2d8"/><stop offset="0.6" stop-color="#c9b9a6"/><stop offset="1" stop-color="#9a5a34"/>
      </linearGradient>
    </defs>
    <polygon points="378,0 824,0 824,397 340,397" fill="url(#front-photo)" role="img" aria-label="Photo: smiling older patient talking with a receptionist at a clinic front desk"/>
    <polygon points="340,397 824,397 824,550 322,550" fill="url(#front-band)"/>
    <polygon points="0,0 378,0 322,550 0,550" fill="url(#front-panel)"/>
  </svg>

  <div class="panel">
    <p class="intro">Make each patient visit a success with</p>
    <div class="rule"></div>
    <div class="title-block">
      <h1 class="title title__main">The INTAKE DESK<br>COMPANION GUIDE</h1>
      <p class="title__sub">for URGENT CARE CENTERS<br>&amp; PHYSICIAN OFFICES</p>
    </div>
    <div class="rule"></div>
    <p class="body-copy">Guaranteed to increase claim revenue. A complete up-to-date resource perfect for training, reference, and best practices. Created by a healthcare administrator with over a decade of experience. A “cheat sheet” of all the information your front desk needs in one place!</p>
    <div class="order">
      <p class="order__label">TO ORDER CALL</p>
      <p class="order__phone">555-014-2290</p>
      <p class="order__price">Only $99.<sup>99</sup></p>
      <p class="order__shipping">plus $7.00 shipping &amp; handling</p>
    </div>
  </div>

  <div class="headline">
    <h2 class="headline__main">EACH PATIENT EXPERIENCE<br>BEGINS at the FRONT DESK</h2>
    <p class="headline__tag">Make a great first impression!</p>
  </div>
</section>

<section class="card card--back">
  <svg class="card__shapes" width="824" height="550" viewBox="0 0 824 550">
    <defs>
      <linearGradient id="back-panel" x1="0" y1="0" x2="1" y2="1">
        <stop offset="0" stop-color="#0b2657"/><stop offset="0.6" stop-color="#143f85"/><stop offset="1" stop-color="#0c2a5c"/>
      </linearGradient>
    </defs>
    <polygon points="0,0 382,0 309,550 0,550" fill="url(#back-panel)"/>
  </svg>

  <div class="panel">
    <div class="rule"></div>
    <div class="title-block">
      <h2 class="title title__main">The INTAKE DESK<br>COMPANION GUIDE</h2>
      <p class="title__sub">for URGENT CARE CENTERS<br>&amp; PHYSICIAN OFFICES</p>
    </div>
    <div class="rule"></div>
    <p class="lead">All the information your front desk needs - in one place! Perfect for raining, reference, best practices, and more.</p>
    <ul class="features">
      <li><svg width="13" height="12" viewBox="0 0 13 12"><path d="M1 6.5 L4.5 10.5 L12 1" fill="none" stroke="#fff" stroke-width="1.8"/></svg>Front desk process flow.</li>
      <li><svg width="13" height="12" viewBox="0 0 13 12"><path d="M1 6.5 L4.5 10.5 L12 1" fill="none" stroke="#fff" stroke-width="1.8"/></svg>Glossary of medical terminology.</li>
      <li><svg width="13" height="12" viewBox="0 0 13 12"><path d="M1 6.5 L4.5 10.5 L12 1" fill="none" stroke="#fff" stroke-width="1.8"/></svg>HIPPA guidelines for office staff.</li>
      <li><svg width="13" height="12" viewBox="0 0 13 12"><path d="M1 6.5 L4.5 10.5 L12 1" fill="none" stroke="#fff" stroke-width="1.8"/></svg>Introduction to insurance carriers, coverage, and plan types.</li>
      <li><svg width="13" height="12" viewBox="0 0 13 12"><path d="M1 6.5 L4.5 10.5 L12 1" fill="none" stroke="#fff" stroke-width="1.8"/></svg>The anatomy of an insurance card.</li>
      <li><svg width="13" height="12" viewBox="0 0 13 12"><path d="M1 6.5 L4.5 10.5 L12 1" fill="none" stroke="#fff" stroke-width="1.8"/></svg>Understanding worker’s compensation &amp; required forms.</li>
    </ul>
    <p class="more">and much more!</p>
  </div>

  <div class="badge">
    <p class="badge__label">To order call</p>
    <p class="badge__phone">555-014-2290</p>
    <p class="badge__price">Only $99.<sup>99</sup></p>
    <p class="badge__shipping">plus $7.00 shipping<br>and handling</p>
  </div>
</section>

</body>
</html>
```